Management Consultancy needs sharp professional services showcased in a brochure

We are a management consultancy specializing on contract management and conflict avoidance services requiring a professional brochure showcasing our services to prospective clients.

Attached are a selection of existing stationary and the colour scheme.

Further details on our company can be found at www.velto-advisory-partners.com
Updates

Preference is for bi-fold, however, innovative tri-fold will be considered. Added Monday, August 7, 2017

Target Market(s)

Construction companies, consultants, developers, oil and gas service providers, NGO's, SME's.

Industry/Entity Type

Management

Requirements
Must have
• High degree of professionalism with eye catching, sharp detail. No frils.
• Colour scheme as per the attachments
• Font as per attachments - Century Gothic
• Details of our company and services
Nice to have
• Open to ideas, thinking along the lines of a car brochure type design.
• Bi-fold preferred, by trifold accepted if innovative.
Should not have
• Remove reference to the United Arab Emirates.
• No cartoon/clipart photos.

```html
<!DOCTYPE html>
<html lang="en">
<head>
<meta charset="utf-8">
<title>Velto Advisory – Brochure Spreads</title>
<link href="https://fonts.googleapis.com/css2?family=Questrial&family=Raleway:wght@400;500;700&display=swap" rel="stylesheet">
<style>
:root{
  --navy:#232a42;
  --red:#b8282e;
  --backdrop:#a4a4a4;
  --paper:#f7f7f7;
  --paper-grey:#ebebeb;
  --panel:rgba(232,232,232,.9);
  --ink:#3a3a3a;
  --puzzle:#1f2660;
}
*{margin:0;padding:0;box-sizing:border-box}
html,body{width:1200px;height:922px;overflow:hidden}
body{background:var(--backdrop);font-family:"Questrial",sans-serif;color:var(--ink);position:relative}
.spread{position:absolute;left:67px;width:1066px;box-shadow:0 2px 6px rgba(0,0,0,.35);overflow:hidden}
.spread--cover{top:71px;height:377px;background:linear-gradient(90deg,var(--paper) 50%,var(--paper-grey) 50%)}
.spread--inside{top:474px;height:377px;background:var(--paper)}
.abs{position:absolute}
.brand{position:absolute;top:34px;width:533px;text-align:center;font-family:"Raleway",sans-serif;font-weight:500;font-size:21px;line-height:24px;letter-spacing:2px;color:var(--navy)}
.brand__dot{display:block;width:28px;height:28px;border-radius:50%;background:var(--navy);margin:0 auto 12px}
.photo-strip{position:absolute;top:127px;left:0;width:1066px;height:161px;display:flex}
.photo{flex:1;height:100%}
.ph-globe{background:radial-gradient(circle at 45% 55%,#bdbdbd 0,#555 45%,#222 60%,#444 100%)}
.ph-bulbs{background:radial-gradient(ellipse at 55% 45%,#e0e0e0 0,#777 30%,#111 75%)}
.ph-hand-r{background:linear-gradient(120deg,#fff 35%,#6d7390 60%,var(--puzzle) 80%)}
.ph-hand-l{background:linear-gradient(300deg,#fff 35%,#6d7390 60%,var(--puzzle) 80%)}
.ph-city{background:linear-gradient(180deg,#cfcfcf 0,#777 50%,#2a2a2a 100%)}
.ph-office{background:linear-gradient(90deg,#e8ecec 0,#c9d2cf 60%,#9fb1a6 100%)}
.band{position:absolute;top:295px;left:0;width:1066px;height:82px;background:var(--navy)}
.band__locs{position:absolute;left:150px;width:234px;top:30px;text-align:center;color:#dfe1e8;font-size:5px;letter-spacing:.3px}
.band__locs i{color:var(--red);font-style:normal;padding:0 3px}
.band__rule{position:absolute;left:150px;width:234px;top:40px;border-top:1px solid #8b90a3}
.band__contact{position:absolute;left:140px;width:254px;top:44px;text-align:center;color:#dfe1e8;font-size:5px}
.band__title{position:absolute;left:533px;width:533px;top:20px;text-align:center;color:#fff;font-size:17px;letter-spacing:2.4px}
.band__web{position:absolute;left:533px;width:533px;top:50px;text-align:center;color:#fff;font-size:11px}
.band__web b,.band__contact b{font-weight:700;font-family:"Raleway",sans-serif}
.spine{position:absolute;top:0;width:60px;height:377px;background:var(--navy)}
.spine__name{position:absolute;font-family:"Raleway",sans-serif;font-weight:500;font-size:19px;letter-spacing:1.5px;color:#fff;white-space:nowrap;text-transform:uppercase}
.spine--left{left:0}
.spine--left .spine__name{left:30px;top:30px;transform-origin:0 0;transform:rotate(90deg) translate(0,-50%)}
.spine--right{left:1005px}
.spine--right .spine__name{left:30px;bottom:30px;transform-origin:0 100%;transform:rotate(-90deg) translate(0,50%)}
.tag{position:absolute;background:var(--red);color:#fff;font-family:"Raleway",sans-serif;font-weight:700;font-size:19px;padding:6px 12px;height:32px;line-height:20px}
.tag span{font-weight:400}
.panel{position:absolute;background:var(--panel);font-size:5.3px;line-height:7px;color:#444}
.panel p{margin-bottom:6px}
.panel ul{list-style:none;margin:2px 0 6px}
.panel li{padding-left:10px;position:relative}
.panel li::before{content:"";position:absolute;left:0;top:1px;width:0;height:0;border-left:3px solid transparent;border-right:3px solid transparent;border-bottom:5px solid var(--red)}
.cols{display:flex;gap:14px}
.cols>div{flex:1}
.intro{position:absolute;left:60px;top:240px;width:423px;height:137px;background:#fff;padding:28px 26px 0 33px;font-size:5.3px;line-height:8.4px;color:#444}
.quote{margin-top:16px;color:var(--red);font-size:13.5px;line-height:15.5px;position:relative;padding-left:10px}
.quote::before{content:"\201C";position:absolute;left:-6px;top:-4px;font-size:28px;font-family:"Raleway",sans-serif}
.quote::after{content:"\201D";font-size:28px;font-family:"Raleway",sans-serif;vertical-align:-12px;margin-left:3px}
.service{position:absolute;left:668px;width:309px;height:90px;display:flex}
.service__label{width:49px;background:var(--red);position:relative}
.service__label span{position:absolute;left:24px;bottom:8px;transform-origin:0 100%;transform:rotate(-90deg);color:#fff;font-size:11px;line-height:11px;text-transform:uppercase;white-space:nowrap}
.service__photo{width:113px;background:linear-gradient(90deg,#fff 0,#6c7290 35%,var(--puzzle) 50%,#fff 60%,var(--puzzle) 80%,#ddd 100%)}
.service__list{flex:1;background:var(--navy);color:#e4e6ee;font-size:5.5px;line-height:7px;list-style:none;padding:18px 10px 0 16px}
.service__list li{margin-bottom:7px;position:relative}
.service__list li::before{content:"";position:absolute;left:-9px;top:0;width:0;height:0;border-left:3px solid transparent;border-right:3px solid transparent;border-bottom:5px solid #e4e6ee}
</style>
</head>
<body>

<section class="spread spread--cover">
  <div class="brand" style="left:0"><span class="brand__dot"></span>VELTO ADVISORY</div>
  <div class="brand" style="left:533px"><span class="brand__dot"></span>VELTO ADVISORY</div>

  <div class="photo-strip">
    <div class="photo ph-globe" role="img" aria-label="Black and white photo of a desk globe"></div>
    <div class="photo ph-bulbs" role="img" aria-label="Row of light bulbs with one glowing"></div>
    <div class="photo ph-hand-r" role="img" aria-label="Hand holding a blue puzzle piece"></div>
    <div class="photo ph-hand-l" role="img" aria-label="Hand holding the matching blue puzzle piece"></div>
    <div class="photo ph-city" role="img" aria-label="Silhouettes of people at an office window over a city"></div>
    <div class="photo ph-office" role="img" aria-label="Bright office with colleagues by a window"></div>
  </div>

  <div class="band">
    <div class="band__locs">UNITED KINGDOM <i>•</i> IRELAND <i>•</i> BRAZIL</div>
    <div class="band__rule"></div>
    <div class="band__contact">Velto Advisory Limited · E: jmoreau@velto-advisory-partners.com · www.<b>velto-advisory-partners</b>.com</div>
    <div class="band__title">THE CONTRACT &amp; CONFLICT ADVISORY</div>
    <div class="band__web">www.<b>velto-advisory-partners</b>.com</div>
  </div>
</section>

<section class="spread spread--inside">
  <div class="spine spine--left"><span class="spine__name">Velto Advisory</span></div>

  <div class="abs ph-city" style="left:60px;top:0;width:579px;height:240px" role="img" aria-label="Black and white photo of business people silhouetted in a glass office overlooking a city"></div>
  <div class="tag" style="left:100px;top:46px">ABOUT <span>US</span></div>
  <div class="panel" style="left:100px;top:78px;width:393px;height:117px;padding:13px 12px">
    <div class="cols">
      <div>
        <p>We are an experienced contract and conflict advisory firm providing global contract performance solutions and conflict management to:</p>
        <ul><li>international development organisations;</li><li>construction industry;</li><li>oil and gas industry; and</li><li>government sectors.</li></ul>
        <p>Observing the standard of advisory services and the size of contract engagements and conflicts, we see the opportunity to make things better: better engagements, better awareness, better performance, which all lead to better value in financial benefit and relationships. We firmly believe in party success in a non litigious environment.</p>
      </div>
      <div>
        <p>Our services are delivered through an integrated management advisory model, with a single point of contact and responsibility, and focused attention to detail. We provide advisory services and solutions resolving past and current claims, and in doing so preparing our clients for a conflict free future based on our core principles of integrity, equality and strength, ensuring compliance and experience at an intimate professional level. We aim to have our clients feel our principles in our presence and in our advice, giving the service which is deserved.</p>
        <p>Our clients range from global Fortune 500 companies, international contractors to government bodies and authorities.</p>
      </div>
    </div>
  </div>

  <div class="intro">
    <p>Velto Advisory is more than just a professional advisory consultancy; we are an integrated professional team with deep domain expertise, industry knowledge and the ability to work across multiple jurisdictions supported by a wide professional network. We forge strong client partnerships and in doing so, we develop and maintain these relationships through performance and delivery of professional services which create and maximise value for our clients. Through our unique approach to contract and conflict management, we want the best for our clients to ensure that contract integrity, compliance and performance is maintained with the upmost faith, based around our principles.</p>
    <p class="quote">If value, whether financial or relationship is not achieved, then we are not finished, we have only just begun.</p>
  </div>
  <div class="abs ph-globe" style="left:483px;top:240px;width:156px;height:137px" role="img" aria-label="Black and white photo of a desk globe"></div>

  <div class="abs" style="left:639px;top:0;width:366px;height:146px;background:linear-gradient(160deg,#5a5a5a,#bdbdbd 55%,#e6e6e6)" role="img" aria-label="Black and white photo of a business handshake"></div>
  <div class="tag" style="left:667px;top:20px">ABOUT <span>US</span></div>
  <div class="panel" style="left:667px;top:52px;width:310px;height:94px;padding:9px 9px">
    <p>Every contract has at least two parties; every party has a goal, and every goal matters. Each party must work in equilibrium as a contractual partnership or alliance. It is on this premise we aim to deliver truly mutual agreements, maintaining the contract integrity from inception through the contract life, and where we are not party to the original agreement, we provide effective solutions to contractual conflict via our unique mediation methodology at all positions of the conflict cycle and aim to enhance all aspects of contract performance by effective audit and management.</p>
    <p>We believe that a proactive approach to contract management creates transparency and trust, and maintains relationships and builds on them for the future whilst cultivating significant value to your business transactions and addressing real and relevant issues, providing and implementing effective solutions. We believe that avoidance of contractual conflict and timely resolution on escalation is paramount in the effectiveness of any agreement.</p>
  </div>

  <div class="service" style="top:168px">
    <div class="service__label"><span>Conflict<br>Advisory</span></div>
    <div class="service__photo" role="img" aria-label="Two hands bringing blue puzzle pieces together"></div>
    <ul class="service__list"><li>Restoration and Mediation Services.</li><li>Shuttle Diplomacy Services and In Persona Intermediary Services.</li><li>Negotiation Support Services.</li><li>Workplace/Corporate Mediation Services.</li></ul>
  </div>
  <div class="service" style="top:266px">
    <div class="service__label"><span>Contract<br>Advisory</span></div>
    <div class="service__photo" role="img" aria-label="Two hands bringing blue puzzle pieces together"></div>
    <ul class="service__list"><li>Restoration and Mediation Services.</li><li>Shuttle Diplomacy Services and In Persona Intermediary Services.</li><li>Negotiation Support Services.</li><li>Workplace/Corporate Mediation Services.</li></ul>
  </div>

  <div class="spine spine--right"><span class="spine__name">Velto Advisory</span></div>
</section>

</body>
</html>
```